M25 Billboard Advert Required Please

I need an advert for a motorway Billboard on the M25 , the advert should show the following in big letters:
GUTTER CLEANING
DALRYNFLUES.COM and a small logo off to the side (Our logo is attached)

The printer has requested the following (Important please) the advert has to be
pdf file / 300 dpi/landscape orientation / scaled to a minimum 25% advert size ( this particular site is 22ft x 10ft so 25% of this please). Please also make sure that the artwork is embedded and outlined correctly if this is incorrect it will affect the printing of the banner.

Target Market(s)

General Public

Industry/Entity Type

Gutter Cleaning

Requirements
Should not have
• No Change to our Logo

```html
<!DOCTYPE html>
<html lang="en">
<head>
<meta charset="utf-8">
<title>Dalryn Flues – Gutter Cleaning Billboard</title>
<link href="https://fonts.googleapis.com/css2?family=Montserrat:wght@700;800&family=Open+Sans:wght@700&display=swap" rel="stylesheet">
<style>
  :root {
    --brand-red: #c1121f;
    --ink: #1d1d1f;
    --paper: #ffffff;
    --backdrop: #f2f2f2;
    --tile-stroke: #b3141f;
  }
  * { margin: 0; padding: 0; box-sizing: border-box; }
  html, body {
    width: 787px;
    height: 1200px;
    overflow: hidden;
    background: var(--backdrop);
  }
  body {
    display: flex;
    align-items: center;
    justify-content: center;
  }
  .billboard {
    position: relative;
    width: 747px;
    height: 339px;
    background: var(--paper);
    overflow: hidden;
    box-shadow: 0 8px 22px rgba(0, 0, 0, 0.28);
    font-family: "Montserrat", Arial, sans-serif;
  }
  .brand {
    position: absolute;
    left: 36px;
    top: 22px;
    display: flex;
    align-items: center;
    gap: 10px;
  }
  .brand-square {
    width: 22px;
    height: 22px;
    background: var(--ink);
  }
  .brand-name {
    font-weight: 800;
    font-size: 32px;
    color: var(--ink);
    letter-spacing: -0.5px;
  }
  .tagline {
    position: absolute;
    left: 36px;
    top: 82px;
    font-family: "Open Sans", Arial, sans-serif;
    font-weight: 700;
    font-size: 15px;
    color: var(--ink);
  }
  .headline {
    position: absolute;
    left: 32px;
    top: 100px;
    font-weight: 800;
    line-height: 0.92;
  }
  .headline-primary {
    display: block;
    font-size: 68px;
    color: var(--brand-red);
    letter-spacing: -1px;
  }
  .headline-secondary {
    display: block;
    font-size: 53px;
    color: var(--ink);
    letter-spacing: -1px;
  }
  .phone-band {
    position: absolute;
    left: 0;
    top: 227px;
    width: 505px;
    height: 48px;
  }
  .phone-number {
    position: absolute;
    left: 33px;
    top: 229px;
    height: 44px;
    line-height: 44px;
    font-weight: 800;
    font-size: 38px;
    color: var(--paper);
    letter-spacing: 0.5px;
  }
  .website {
    position: absolute;
    left: 34px;
    top: 286px;
    font-weight: 800;
    font-size: 25px;
    color: var(--ink);
    letter-spacing: 1px;
  }
  .photo-mosaic {
    position: absolute;
    left: 0;
    top: 0;
    width: 747px;
    height: 339px;
  }
  .tile {
    stroke: var(--tile-stroke);
    stroke-width: 3;
  }
</style>
</head>
<body>
  <main class="billboard">
    <svg class="phone-band" viewBox="0 0 505 48" aria-hidden="true">
      <polygon points="0,0 470,0 505,48 0,48" fill="var(--brand-red)"/>
    </svg>

    <svg class="photo-mosaic" viewBox="0 0 747 339">
      <defs>
        <linearGradient id="tone-tools" x1="0" y1="0" x2="1" y2="1">
          <stop offset="0" stop-color="#e9e4dc"/><stop offset="1" stop-color="#8a9a5b"/>
        </linearGradient>
        <linearGradient id="tone-roof-worker" x1="0" y1="0" x2="1" y2="1">
          <stop offset="0" stop-color="#7d8a6a"/><stop offset="1" stop-color="#c9c3b6"/>
        </linearGradient>
        <linearGradient id="tone-gutter" x1="0" y1="0" x2="1" y2="1">
          <stop offset="0" stop-color="#6f6a66"/><stop offset="1" stop-color="#a9a7a3"/>
        </linearGradient>
        <linearGradient id="tone-ladder" x1="0" y1="0" x2="1" y2="1">
          <stop offset="0" stop-color="#9fb6cf"/><stop offset="0.45" stop-color="#8a6a55"/><stop offset="1" stop-color="#5c4638"/>
        </linearGradient>
        <linearGradient id="tone-house" x1="0" y1="0" x2="1" y2="1">
          <stop offset="0" stop-color="#7fa7d8"/><stop offset="1" stop-color="#a5563a"/>
        </linearGradient>
        <linearGradient id="tone-street" x1="0" y1="0" x2="1" y2="1">
          <stop offset="0" stop-color="#6c7d57"/><stop offset="1" stop-color="#3d3f44"/>
        </linearGradient>
        <linearGradient id="tone-pole" x1="0" y1="0" x2="1" y2="1">
          <stop offset="0" stop-color="#5f8a3e"/><stop offset="1" stop-color="#2b2b2b"/>
        </linearGradient>
      </defs>

      <g role="img" aria-label="Photo: gutter sealant gun being used on a gutter joint">
        <rect class="tile" x="368" y="-44" width="112" height="112" rx="10" fill="url(#tone-tools)" transform="rotate(45 424 12)"/>
      </g>
      <g role="img" aria-label="Photo: worker in hard hat and hi-vis vest clearing a roof gutter">
        <rect class="tile" x="445.5" y="34.5" width="113" height="113" rx="10" fill="url(#tone-roof-worker)" transform="rotate(45 502 91)"/>
      </g>
      <g role="img" aria-label="Photo: close view of a cleared gutter along a roof edge">
        <rect class="tile" x="525" y="-32" width="112" height="112" rx="10" fill="url(#tone-gutter)" transform="rotate(45 581 24)"/>
      </g>
      <g role="img" aria-label="Photo: technician on a ladder cleaning the gutter of a brick house">
        <rect class="tile" x="598.5" y="53.5" width="233" height="233" rx="12" fill="url(#tone-ladder)" transform="rotate(45 715 170)"/>
      </g>
      <g role="img" aria-label="Photo: large red-brick house with tall chimneys">
        <rect class="tile" x="369" y="127" width="102" height="102" rx="10" fill="url(#tone-house)" transform="rotate(45 420 178)"/>
      </g>
      <g role="img" aria-label="Photo: rooftop gutter view above a residential street">
        <rect class="tile" x="442" y="200" width="120" height="120" rx="10" fill="url(#tone-street)" transform="rotate(45 502 260)"/>
      </g>
      <g role="img" aria-label="Photo: technician using a gutter vacuum pole from the ground">
        <rect class="tile" x="549" y="265" width="112" height="112" rx="10" fill="url(#tone-pole)" transform="rotate(45 605 321)"/>
      </g>
    </svg>

    <div class="brand">
      <span class="brand-square" aria-hidden="true"></span>
      <span class="brand-name">Dalryn Flues</span>
    </div>
    <p class="tagline">Clean gutters protect your property</p>
    <h1 class="headline">
      <span class="headline-primary">GUTTER</span>
      <span class="headline-secondary">CLEANING</span>
    </h1>
    <p class="phone-number">44 800 015 7391</p>
    <p class="website">WWW.DALRYNFLUES.COM</p>
  </main>
</body>
</html>
```